DORV2020 Save the date post card

Take the look and feel of the logo you designed and create a save the date postcard. 7L" by 5"H - print ready file with crop marks and bleeds.

Colors

Designer to choose colors to be used in the design.

Requirements
Must have
• The logo somewhere on the card.
• The following text:
• Save the Date
• June 1 - 4
• dorvsummit.ca
• Stronger United: Gather. Spark. Flourish.
Nice to have
• The following text:
• Vision: The vision of the DORV 2020 conference is to improve patient care by bringing together the Canadian Emergency Medicine community.
• Learning Objectives:
• By the end of the conference, delegates will be able to;
• • Apply up to date evidence to inform clinical decisions;
• • Acquire practical skills by participating in interactive sessions;
• • Connect and collaborate with other delegates;
• • Consider strategies to ensure career longevity; and
• • Influence the future direction of Emergency Medicine in Canada

```html
<!DOCTYPE html>
<html lang="en">
<head>
<meta charset="utf-8">
<title>DORV2020 Save the Date Postcard</title>
<link href="https://fonts.googleapis.com/css2?family=Questrial&family=Roboto+Condensed:wght@700&display=swap" rel="stylesheet">
<style>
  :root {
    --canvas: #2a3140;
    --blue: #1c95d3;
    --red: #e0202e;
    --ink: #555a60;
    --muted: #8a8f95;
    --paper: #ffffff;
    --paper-grey: #f2f2f2;
    --rule: #9a9ea3;
    --purple: #7d3fa6;
  }
  * { box-sizing: border-box; margin: 0; padding: 0; }
  html, body { width: 1200px; height: 900px; overflow: hidden; }
  body {
    background: var(--canvas);
    font-family: "Questrial", "Century Gothic", sans-serif;
    display: flex;
    align-items: center;
    justify-content: center;
    gap: 40px;
  }
  .postcard {
    width: 560px;
    height: 400px;
    position: relative;
    overflow: hidden;
    background: var(--paper);
  }

  /* Front */
  .front { background: var(--paper-grey); }
  .front__topband { height: 8px; background: var(--blue); }
  .front__header {
    position: relative;
    height: 128px;
    background: linear-gradient(90deg, #ececec 0%, #f6f6f6 45%, #efefef 100%);
  }
  .brand {
    position: absolute;
    left: 30px;
    top: 52px;
    display: flex;
    flex-direction: column;
    gap: 4px;
  }
  .brand__row { display: flex; align-items: center; gap: 8px; }
  .brand__dot { width: 14px; height: 14px; border-radius: 50%; background: var(--purple); }
  .brand__name { font-size: 24px; color: var(--purple); letter-spacing: 0.5px; }
  .brand__sub { font-size: 9px; color: var(--muted); padding-left: 40px; }

  .headline {
    position: absolute;
    left: 257px;
    top: 32px;
    width: 274px;
    text-align: center;
  }
  .headline__rule { height: 1px; background: var(--blue); }
  .headline__title {
    font-family: "Roboto Condensed", "Arial Narrow", sans-serif;
    font-weight: 700;
    font-size: 42px;
    line-height: 1;
    white-space: nowrap;
    color: var(--blue);
    margin: 8px 0 4px;
  }
  .headline__date-row { display: flex; align-items: center; gap: 14px; }
  .headline__date-row .headline__rule { flex: 1; }
  .headline__date {
    background: var(--blue);
    color: #fff;
    font-family: "Roboto Condensed", "Arial Narrow", sans-serif;
    font-weight: 700;
    font-size: 13px;
    line-height: 1.35;
    padding: 1px 26px;
    white-space: nowrap;
    letter-spacing: 0.5px;
  }

  .photos { display: flex; height: 178px; }
  .photos__item { flex: 1; }
  .photos__item--training { background: linear-gradient(135deg, #9aa0a8 0%, #6b7480 50%, #3f4c63 100%); }
  .photos__item--networking { flex: 1.15; background: linear-gradient(135deg, #7a5a3a 0%, #a98a66 45%, #4a4f5a 100%); border-left: 1px solid #fff; }
  .front__redline { height: 4px; background: var(--red); }

  .tagline { text-align: center; padding-top: 18px; }
  .tagline__title { font-size: 25px; color: var(--blue); letter-spacing: 3px; line-height: 1.1; }
  .tagline__words { font-size: 13px; color: var(--ink); margin-top: 5px; }
  .tagline__dot { color: var(--red); margin: 0 8px; }

  /* Back */
  .back { background: linear-gradient(180deg, #ffffff 0%, #ffffff 55%, #f1f1f1 100%); }
  .back__content {
    position: absolute;
    left: 20px;
    top: 22px;
    width: 310px;
    color: var(--ink);
    font-size: 12.5px;
    line-height: 1.3;
  }
  .back__label { color: var(--blue); }
  .back__vision { margin-bottom: 10px; }
  .back__objectives-title { color: var(--blue); margin-bottom: 2px; }
  .objectives { list-style: none; margin-top: 6px; }
  .objectives li { position: relative; padding-left: 10px; margin-bottom: 4px; }
  .objectives li::before {
    content: "";
    position: absolute;
    left: 0; top: 6px;
    width: 4px; height: 4px;
    border-radius: 50%;
    background: var(--blue);
  }
  .stamp {
    position: absolute;
    right: 24px;
    top: 48px;
    width: 63px;
    height: 63px;
    border: 1px solid var(--rule);
  }
  .address { position: absolute; right: 32px; top: 183px; width: 188px; }
  .address__line { height: 1px; background: var(--rule); margin-bottom: 43px; }
  .back__url { position: absolute; right: 32px; bottom: 48px; font-size: 13px; color: var(--blue); }
  .back__bottomband { position: absolute; left: 0; right: 0; bottom: 0; height: 8px; background: var(--blue); }
</style>
</head>
<body>

  <section class="postcard front" aria-label="Postcard front">
    <div class="front__topband"></div>
    <header class="front__header" role="img" aria-label="Faint photo of conference delegates behind the header">
      <div class="brand">
        <div class="brand__row">
          <span class="brand__dot"></span>
          <span class="brand__name">DORV2020</span>
        </div>
        <span class="brand__sub">Ottawa June 1 - 4</span>
      </div>
      <div class="headline">
        <div class="headline__rule"></div>
        <h1 class="headline__title">SAVE THE DATE</h1>
        <div class="headline__date-row">
          <div class="headline__rule"></div>
          <span class="headline__date">JUNE 1 - 4</span>
          <div class="headline__rule"></div>
        </div>
      </div>
    </header>
    <div class="photos">
      <div class="photos__item photos__item--training" role="img" aria-label="Photo of a hands-on simulation training session"></div>
      <div class="photos__item photos__item--networking" role="img" aria-label="Photo of two delegates talking at a networking reception"></div>
    </div>
    <div class="front__redline"></div>
    <div class="tagline">
      <p class="tagline__title">STRONGER UNITED</p>
      <p class="tagline__words">Gather<span class="tagline__dot">•</span>Spark<span class="tagline__dot">•</span>Flourish</p>
    </div>
  </section>

  <section class="postcard back" aria-label="Postcard back">
    <div class="back__content">
      <p class="back__vision"><span class="back__label">Vision:</span> The vision of the DORV 2020 conference is to improve patient care by bringing together the Canadian Emergency Medicine community.</p>
      <p class="back__objectives-title">Learning Objectives:</p>
      <p>By the end of the conference, delegates will be able to;</p>
      <ul class="objectives">
        <li>Apply up to date evidence to inform clinical decisions;</li>
        <li>Acquire practical skills by participating in interactive sessions;</li>
        <li>Connect and collaborate with other delegates;</li>
        <li>Consider strategies to ensure career longevity; and</li>
        <li>Influence the future direction of Emergency Medicine in Canada</li>
      </ul>
    </div>
    <div class="stamp"></div>
    <div class="address">
      <div class="address__line"></div>
      <div class="address__line"></div>
      <div class="address__line"></div>
      <div class="address__line"></div>
    </div>
    <p class="back__url">dorvsummit.ca</p>
    <div class="back__bottomband"></div>
  </section>

</body>
</html>
```